Property Investment eBook Cover

I am a long established Australian property investment adviser, analyst and consultant who is now in semi-retired mode and have re-branded to reflect a more casual and personal approach to advising my property investor clients. I am writing a 'revised edition' to a book written in partnership with my father 20 years ago and need an eBook Cover for this new edition. The eBook will be uploaded to all the regular Australian providers (Tarvo Reader, Quillet Epage, Zeni, Pagemarsh)

The 3 key elements in the book cover are:

Title: The Riches Engine of Land. The word 'Property' should be larger and more prominent. eg "The Wealth Power of" could be 1/3 the size of "Property" - with both justified left

Edition: Sydney 2021. "Sydney 2021" should be the focus and dominant imagery of the eBook cover and more prominent than the Title or Author

Author: Glen Markby, The Housing Numbers Guide. The word "Author" should not appear. "The Housing Numbers Guide" should appear underneath Glen Markby and justified to Glen Markby, therefore a smaller font.

The cover should be simple, but eye-catching. No property images, more of an abstract background, than a background with an image. Our preferred colour palette is more blues/greens. Prefer SerifFonts

Copy of book published 20 years ago attached for reference only

```html
<!DOCTYPE html>
<html lang="en">
<head>
<meta charset="utf-8">
<title>The Riches Engine of Land — Sydney 2021</title>
<link rel="stylesheet" href="https://fonts.googleapis.com/css2?family=Anton&family=Cinzel:wght@400;600;700&display=swap">
<style>
  :root {
    --gold-light: #f3d15a;
    --gold: #e6b52f;
    --gold-deep: #c9951c;
    --rust: #8b3a16;
    --blue: #1f4592;
    --blue-deep: #183a80;
    --white: #ffffff;
    --outline: #4a3830;
    --yellow: #f4ee1e;
  }
  html, body {
    margin: 0;
    padding: 0;
    width: 750px;
    height: 1200px;
    overflow: hidden;
    background: var(--blue);
  }
  .cover {
    position: relative;
    width: 750px;
    height: 1200px;
    overflow: hidden;
    background: var(--blue);
  }
  .gold-band {
    position: absolute;
    left: 0; top: 0;
    width: 750px;
    height: 450px;
    background:
      radial-gradient(ellipse at 30% 20%, var(--gold-light) 0%, transparent 60%),
      radial-gradient(ellipse at 85% 70%, var(--gold-deep) 0%, transparent 55%),
      linear-gradient(160deg, var(--gold) 0%, var(--gold-light) 45%, var(--gold) 100%);
  }
  .blue-field {
    position: absolute;
    left: 0; top: 380px;
    width: 750px;
    height: 820px;
  }
  .title-lead, .title-main {
    position: absolute;
    left: 54px;
    margin: 0;
    font-family: "Anton", "Oswald", sans-serif;
    color: var(--rust);
    text-transform: uppercase;
    line-height: 1;
    font-weight: 400;
  }
  .title-lead {
    top: 28px;
    font-size: 46px;
    letter-spacing: 0.5px;
  }
  .title-main {
    top: 158px;
    font-size: 222px;
    letter-spacing: 2px;
  }
  .edition {
    position: absolute;
    left: 0;
    width: 750px;
    text-align: center;
    margin: 0;
    font-family: "Cinzel", "Times New Roman", serif;
    font-weight: 700;
    color: var(--white);
    line-height: 1;
    text-shadow: 3px 3px 0 var(--outline), -1px -1px 0 var(--outline), 1px -1px 0 var(--outline), -1px 1px 0 var(--outline);
  }
  .edition-city {
    top: 518px;
    font-size: 138px;
    letter-spacing: -2px;
  }
  .edition-year {
    top: 640px;
    font-size: 300px;
    letter-spacing: -14px;
  }
  .divider {
    position: absolute;
    left: 0; top: 972px;
    width: 750px;
    height: 4px;
    background: var(--white);
  }
  .author {
    position: absolute;
    left: 0; top: 1036px;
    width: 750px;
    text-align: center;
  }
  .author-name {
    margin: 0;
    font-family: "Cinzel", "Times New Roman", serif;
    font-weight: 400;
    font-size: 58px;
    color: var(--white);
    letter-spacing: 3px;
    line-height: 1;
  }
  .author-role {
    margin: 18px 0 0;
    font-family: "Cinzel", "Times New Roman", serif;
    font-weight: 400;
    font-size: 30px;
    color: var(--yellow);
    letter-spacing: 2px;
    text-transform: uppercase;
    line-height: 1;
  }
</style>
</head>
<body>
  <main class="cover">
    <div class="gold-band" role="img" aria-label="Warm gold textured paper background"></div>

    <svg class="blue-field" width="750" height="820" viewBox="0 0 750 820" aria-hidden="true">
      <path fill="#2a56a6" d="M0 32 L40 30 L70 26 L95 33 L130 29 L150 22 L185 28 L220 24 L260 31 L300 34 L335 40 L365 43 L395 30 L420 34 L450 28 L480 24 L520 22 L560 10 L600 14 L640 18 L680 20 L710 16 L750 12 L750 820 L0 820 Z"/>
      <path fill="#1f4592" d="M0 40 L45 38 L80 35 L110 40 L150 32 L190 36 L230 33 L270 39 L310 42 L350 48 L385 38 L420 41 L460 35 L500 31 L540 30 L575 20 L615 24 L655 26 L700 25 L750 20 L750 820 L0 820 Z"/>
    </svg>

    <h1 class="title">
      <span class="title-lead">The Riches Engine of</span>
      <span class="title-main">Land</span>
    </h1>

    <h2 class="edition edition-city">Sydney</h2>
    <p class="edition edition-year">2021</p>

    <div class="divider"></div>

    <div class="author">
      <p class="author-name">Glen Markby</p>
      <p class="author-role">The Housing Numbers Guide</p>
    </div>
  </main>
</body>
</html>
```